Cover-Design für Buch gesucht
Die Designerin war sehr engagiert und hat innerhalb kürzester Zeit auf Änderungswünsche reagiert - und das so lange, so detailliert und so geduldig, bis wirklich alles gut war!
Zielgruppe
Ich bin niedergelassene Psychotherapeutin und schreibe nebenher als Hobby. Für mein erstes Buch, das ich im Selbstverlag bei Veltrona Pressdesk veröffentlichen möchte, benötige ich ein aussagekräftiges, ausgefallenes, neugierig machendes Buchcover.
Zielgruppe sind hauptsächlich Krimi-Leser/innen und am Rande hoffentlich ein paar Fantasy-Leser/innen. Altersklasse vermutlich von ca. 20 bis 50 Jahre.
Aufgabenstellung
Das Buch ist eine Mischung aus Krimi und Fantasy. Wobei ich die Vampire ein Stück weit aus dem Bereich der Fantasy rausgeholt und „realistisch“ gemacht habe. Die Vampire sind quasi eine zweite – im Laufe der Evolution parallel zu den Menschen entwickelte – Art von Menschen. Sie werden geboren, leben in echt, können ganz normal verletzt werden und auch sterben. Sie leben in Symbiose mit den Menschen, trinken nachts, wenn die Menschen schlafen, deren Blut und spritzen danach ein hochregeneratives Serum in die Wunde, was die Wunde a) innerhalb kürzester Zeit heilen lässt und b) zusätzlich einige Krankheiten der Menschen heilen kann. Die Vampire haben noch immer ein paar spezielle Fähigkeiten (aber keine wirklich übernatürlichen Fähigkeiten mehr), sind z.B. stärker, attraktiver und deren Wunden heilen wegen ihrer regenerativen Eigenschaften schneller. All diese Fähigkeiten versuche ich „wissenschaftlich/medizinisch“ zu erklären – sofern man etwas nicht Existierendes und in unserer Realität nicht Machbares eben erklären kann.
Im Grunde handelt es sich also nicht mehr um klassische Fantasy, weil die Vampire ja einfach nur eine zweite Art von ganz „normalen“ Menschen sind. Insofern sollte das Buch-Cover vor allem in das Genre Krimi passen, dennoch irgendwie am Rande das Thema Vampir aufgreifen, so dass potentielle Leser erkennen, dass es sich eben nicht um einen ganz normalen Krimi handelt, sondern Vampire eine gewisse Rolle spielen.
Neben dem Kriminalfall (Kinder werden entführt, die Protagonisten müssen herausfinden, wer dies wieso gemacht hat) spielt die Freundschaft zwischen Korinna und Henning eine große Rolle, die sich langsam entwickelnde und intensiver werdende Schüler-Lehrer-Beziehung zwischen Korinna und Udo sowie die sich langsam entwickelnde Liebe zwischen Korinna und Falk. Die Geschichte ist also etwas „weicher“ und vielleicht von den zwischenmenschlichen Themen etwas tiefgründiger als ein einfacher, „knall..

```html
<!DOCTYPE html>
<html lang="de">
<head>
<meta charset="utf-8">
<title>Vermisst in Berlin – Buchcover</title>
<link rel="stylesheet" href="https://fonts.googleapis.com/css2?family=Lato:wght@700;900&family=Stardos+Stencil:wght@700&display=swap">
<style>
  :root {
    --night: #231815;
    --blood: #c20f23;
    --blood-deep: #7a0f18;
    --paper: #ffffff;
    --dusk-top: #f3d3c4;
    --dusk-mid: #de8a6f;
    --dusk-low: #c0202a;
    --ink: #1a1210;
  }
  html, body {
    margin: 0;
    padding: 0;
    overflow: hidden;
    background: var(--night);
  }
  .cover {
    position: relative;
    width: 750px;
    height: 1200px;
    background: var(--night);
    overflow: hidden;
  }
  .author {
    position: absolute;
    left: 0;
    top: 0;
    width: 750px;
    height: 140px;
  }
  .author text {
    font-family: "Lato", sans-serif;
    font-weight: 700;
    fill: var(--blood);
  }
  .blood-drips {
    position: absolute;
    left: 348px;
    top: 375px;
    width: 284px;
    height: 380px;
    background: radial-gradient(ellipse 45% 50% at 45% 45%, rgba(170, 24, 34, 0.8), rgba(110, 12, 20, 0.5) 60%, rgba(35, 24, 21, 0) 100%);
  }
  .title {
    position: absolute;
    left: 0;
    top: 0;
    width: 750px;
    height: 1200px;
  }
  .title text {
    font-family: "Stardos Stencil", serif;
    font-weight: 700;
    fill: var(--paper);
  }
  .skyline {
    position: absolute;
    left: 0;
    top: 905px;
    width: 750px;
    height: 295px;
    background: linear-gradient(to bottom, var(--dusk-top) 0%, var(--dusk-mid) 50%, var(--dusk-low) 100%);
  }
  .genre {
    position: absolute;
    top: 1126px;
    left: 0;
    width: 750px;
    text-align: center;
    margin: 0;
    font-family: "Lato", sans-serif;
    font-weight: 900;
    font-size: 42px;
    letter-spacing: 6px;
    line-height: 1;
    color: var(--ink);
  }
</style>
</head>
<body>
<main class="cover">
  <svg class="author" viewBox="0 0 750 140" aria-label="Lennart Havel">
    <text x="57" y="113" font-size="78" textLength="636" lengthAdjust="spacingAndGlyphs">LENNART HAVEL</text>
  </svg>

  <div class="skyline" role="img" aria-label="Dunkle Berliner Skyline-Silhouette mit Fernsehturm vor rötlichem Abendhimmel"></div>

  <div class="blood-drips" role="img" aria-label="Zwei Bisswunden, aus denen Blut über den Titel herabrinnt"></div>

  <svg class="title" viewBox="0 0 750 1200" aria-label="Vermisst in Berlin">
    <text x="42" y="672" font-size="125" textLength="653" lengthAdjust="spacingAndGlyphs">VERMISST</text>
    <text x="112" y="767" font-size="80" textLength="82" lengthAdjust="spacingAndGlyphs">IN</text>
    <text x="230" y="797" font-size="125" textLength="465" lengthAdjust="spacingAndGlyphs">BERLIN</text>
  </svg>

  <p class="genre">KRIMI</p>
</main>
</body>
</html>
```